Birchwell Chiropractic, achieve your health goals, get better each day one step at a time

A mobile friendly site, fresh look, easy to navigate, has interface with zq/chirplane, etc. Blog posts. Uses new logo. Content and address to current site is birchwellclinic.net. The current site will give you scope of project for content. The logo is not the final but close. Will upload final next week.
Convey the concept that heath is a process, it does not just happen. We take steps to achieve what we want in life including health.

Target Market(s)

30 to 70 year old. Needing health care

Industry/Entity Type

Health Care

Coding

Coded - Design and coding required

Number of Pages Required

5+ page

Font styles to use
Sans Serif

Colors

Designer to choose colors to be used in the design.

Requirements
Must have
• mobile friendly, easy to navigate, ZQ/Chirplane interface, blog, room for current content
Nice to have
• potential for commerce, statistics
Should not have
• Same old look and feel as everything else out there

```html
<!DOCTYPE html>
<html lang="en">
<head>
<meta charset="utf-8">
<title>Birchwell Chiropractic</title>
<link href="https://fonts.googleapis.com/css2?family=Montserrat:wght@400;600;700&family=Open+Sans:wght@400;600;700&display=swap" rel="stylesheet">
<style>
:root{
  --green:#6fa23b;
  --green-dark:#4d7d22;
  --green-deep:#3e6a1a;
  --blue:#1f9bd7;
  --ink:#3d3d3d;
  --muted:#5c5c5c;
  --line:#e2e2e2;
  --white:#ffffff;
}
*{box-sizing:border-box;margin:0;padding:0}
html,body{width:1200px;height:4724px;overflow:hidden}
body{font-family:"Open Sans",Arial,sans-serif;color:var(--ink);background:var(--white);font-size:13px;line-height:1.45}
.wrap{width:1040px;margin:0 auto;position:relative}
h2.section-title{font-family:"Montserrat",Arial,sans-serif;font-weight:600;font-size:30px;text-align:center;color:var(--green)}
h2.section-title::after{content:"";display:block;width:60px;height:2px;background:currentColor;margin:10px auto 0;opacity:.7}

/* header */
.site-header{height:132px}
.site-header .wrap{display:flex;align-items:center;height:132px}
.brand{display:flex;align-items:center;gap:12px}
.brand-dot{width:54px;height:54px;border-radius:50%;background:var(--green)}
.brand-name{font-family:"Montserrat",Arial,sans-serif;font-weight:700;font-size:26px;color:var(--green-deep)}
.header-call{margin-left:auto;text-align:center;margin-right:90px}
.header-call small,.header-follow small{display:block;font-size:14px;color:var(--green)}
.header-call strong{font-family:"Montserrat",Arial,sans-serif;font-size:26px;color:var(--ink)}
.header-follow{text-align:center}
.social-row{display:flex;gap:5px;margin-top:4px}
.social-row span{width:20px;height:20px;border-radius:3px;background:var(--blue)}
.social-row span:nth-child(1){background:#3b5998}
.social-row span:nth-child(2){background:#d8493a}
.social-row span:nth-child(3){background:#2fa8dc}
.social-row span:nth-child(4){background:#1676b0}

/* nav */
.main-nav{height:33px;background:var(--green)}
.main-nav .wrap{display:flex;align-items:center;height:33px}
.main-nav a{color:var(--white);text-decoration:none;font-size:12px;padding:0 24px;line-height:33px}
.main-nav a.active{background:var(--green-deep)}
.nav-search{margin-left:auto;width:180px;height:20px;background:var(--white);border-radius:2px;display:flex;align-items:center;justify-content:space-between;padding:0 6px;font-size:11px;color:#888}

/* hero */
.hero{height:591px;position:relative;background:linear-gradient(180deg,#c9d2d3 0%,#aebbb8 40%,#7f8f77 70%,#56684a 100%);display:flex;flex-direction:column;align-items:center;justify-content:center;color:var(--white);text-align:center}
.hero h1{font-family:"Montserrat",Arial,sans-serif;font-weight:700;font-size:50px;letter-spacing:1px;margin-top:70px;text-shadow:0 2px 6px rgba(0,0,0,.25)}
.hero p{font-family:"Montserrat",Arial,sans-serif;font-weight:700;font-size:31px;letter-spacing:.5px;text-shadow:0 2px 6px rgba(0,0,0,.25)}
.hero-arrow{position:absolute;top:270px}
.hero-arrow.left{left:56px}.hero-arrow.right{right:56px}
.hero-dots{position:absolute;bottom:28px;display:flex;gap:14px}
.hero-dots span{width:9px;height:9px;border-radius:50%;background:rgba(255,255,255,.55)}
.hero-dots span.on{background:var(--white)}

/* about */
.about{height:709px;padding-top:62px}
.about-body{display:flex;margin-top:38px}
.about-photo-col{width:400px;padding-left:40px;position:relative}
.about-photo{width:270px;height:370px;margin-left:20px;background:linear-gradient(180deg,#f2f2f2,#d7d2cc 60%,#3a3a3a)}
.about-caption{position:relative;width:320px;margin-top:-10px;background:var(--green);color:var(--white);border-radius:30px;text-align:center;font-family:"Montserrat",Arial,sans-serif;font-weight:600;font-size:16px;line-height:1.35;padding:14px 0}
.about-info{flex:1;font-size:11.5px;color:var(--ink)}
.tag{display:inline-block;background:var(--green);color:var(--white);font-family:"Montserrat",Arial,sans-serif;font-weight:700;font-size:15px;letter-spacing:.5px;padding:2px 14px;border-radius:3px;margin:6px 0 8px}
.about-info li{list-style:none;margin-bottom:12px}
.about-pair{display:flex}
.about-pair>div{width:335px}

/* testimonial */
.testimonials{height:355px;background:var(--green);padding-top:60px;color:var(--white)}
.testimonials h2.section-title{color:var(--white)}
.quote-row{display:flex;justify-content:space-between;margin-top:40px}
.quote{width:480px}
.quote blockquote{background:var(--white);color:var(--green);border-radius:14px;padding:12px 16px;font-size:10.5px;line-height:1.4;text-align:center;min-height:100px}
.quote cite{display:block;text-align:center;font-style:normal;font-weight:700;font-size:12px;margin-top:16px}

/* faq */
.faqs{height:763px;background:linear-gradient(180deg,#f3f4f1,#e6e3df 50%,#eef0ec);padding-top:58px}
.faq-grid{display:grid;grid-template-columns:repeat(3,250px);column-gap:70px;row-gap:30px;justify-content:center;margin-top:65px}
.faq h3{background:var(--green);color:var(--white);font-family:"Montserrat",Arial,sans-serif;font-weight:700;font-size:17px;line-height:1.2;text-align:center;height:95px;display:flex;align-items:center;justify-content:center;padding:0 12px}
.faq p{font-size:10.5px;color:var(--ink);height:108px;padding:10px 4px 0;line-height:1.45}
.more-line{position:relative;height:24px;margin-top:8px}
.more-line::before{content:"";position:absolute;left:0;right:0;top:12px;height:1px;background:#bfc7b8}
.more-line span{position:absolute;left:113px;top:0;width:24px;height:24px;border-radius:50%;background:var(--blue);color:var(--white);font-weight:700;font-size:18px;line-height:24px;text-align:center}

/* services */
.services{height:1197px;background:linear-gradient(180deg,#6a9c37,#74a840 50%,#6a9c37);padding-top:62px}
.services h2.section-title{color:var(--white)}
.service-grid{display:grid;grid-template-columns:repeat(3,250px);column-gap:70px;row-gap:122px;justify-content:center;margin-top:64px}
.service-photo{height:205px}
.service h3{background:var(--white);color:var(--green);font-family:"Montserrat",Arial,sans-serif;font-weight:700;font-size:16px;text-align:center;height:34px;line-height:34px;border-bottom:1px solid var(--line)}
.service p{background:var(--white);font-size:10.5px;color:var(--ink);padding:6px 8px;height:80px;line-height:1.4}
.btn-outline{display:block;width:122px;margin:160px auto 0;border:1px solid var(--white);color:var(--white);text-align:center;font-size:12px;padding:6px 0;text-decoration:none}

/* other services */
.other{height:614px;padding-top:70px;position:relative}
.other-grid{display:flex;justify-content:center;gap:105px;margin-top:60px}
.other-item{width:205px;text-align:center}
.other-circle{width:205px;height:205px;border-radius:50%}
.other-item h3{font-family:"Montserrat",Arial,sans-serif;font-weight:700;font-size:16px;color:var(--green);margin-top:14px}
.other-item p{font-size:10.5px;color:var(--ink);height:32px;margin-top:4px;line-height:1.45}
.btn-blue{display:inline-block;background:var(--blue);color:var(--white);font-size:12px;padding:6px 18px;margin-top:14px;text-decoration:none}
.side-arrow{position:absolute;top:285px;width:26px;height:26px;background:#6d6d6d;display:flex;align-items:center;justify-content:center}
.side-arrow.left{left:0}.side-arrow.right{right:0}

/* footer */
.site-footer{height:293px;background:var(--green);color:var(--white);padding-top:55px}
.footer-cols{display:flex;justify-content:space-between;padding:0 8px}
.footer-cols h4{font-family:"Montserrat",Arial,sans-serif;font-weight:700;font-size:14px;margin-bottom:14px}
.quick-links li{list-style:none;font-size:11px;margin-bottom:5px;display:flex;align-items:center;gap:8px}
.quick-links li::before{content:"";width:5px;height:5px;background:var(--white);border-radius:50%}
.contact-list{font-size:11px;line-height:1.5}
.contact-list div{display:flex;align-items:center;gap:6px}
.contact-list i{width:9px;height:9px;border-radius:50%;background:var(--white);display:inline-block}
.map{width:210px;height:150px;background:linear-gradient(135deg,#e9ece6,#d6dcd2)}
.follow-icons{display:flex;gap:14px;margin-bottom:16px}
.follow-icons span{width:14px;height:14px;background:var(--white);border-radius:2px}
.badge-row{display:flex;align-items:center;gap:8px;margin-bottom:14px}
.badge-row span{width:40px;height:40px;border-radius:50%;background:#dfe9d3}
.footer-call{font-family:"Montserrat",Arial,sans-serif;font-weight:700;font-size:20px;line-height:1.2}
.footer-bar{height:37px;background:var(--green-deep);color:var(--white);font-size:11px;text-align:center;line-height:37px}
</style>
</head>
<body>

<header class="site-header">
  <div class="wrap">
    <div class="brand"><span class="brand-dot"></span><span class="brand-name">Birchwell Chiropractic</span></div>
    <div class="header-call"><small>Call us</small><strong>555.014.2290</strong></div>
    <div class="header-follow"><small>Follow Us</small><div class="social-row"><span></span><span></span><span></span><span></span></div></div>
  </div>
</header>

<nav class="main-nav">
  <div class="wrap">
    <a class="active" href="#">HOME</a><a href="#">ABOUT US</a><a href="#">TESTIMONIALS</a><a href="#">FAQS</a><a href="#">RESOURCES</a><a href="#">CONTACT US</a>
    <div class="nav-search">Search...<svg width="10" height="10" viewBox="0 0 10 10"><circle cx="4" cy="4" r="3" fill="none" stroke="#666" stroke-width="1.4"/><line x1="6.2" y1="6.2" x2="9.3" y2="9.3" stroke="#666" stroke-width="1.4"/></svg></div>
  </div>
</nav>

<section class="hero" role="img" aria-label="Woman in a balance pose on a misty mountain top">
  <svg class="hero-arrow left" width="24" height="44" viewBox="0 0 24 44"><polyline points="21,2 3,22 21,42" fill="none" stroke="#fff" stroke-width="3"/></svg>
  <h1>ACHIEVE YOUR HEALTH GOALS</h1>
  <p>GET BETTER EACH DAY ONE STEP AT A TIME</p>
  <svg class="hero-arrow right" width="24" height="44" viewBox="0 0 24 44"><polyline points="3,2 21,22 3,42" fill="none" stroke="#fff" stroke-width="3"/></svg>
  <div class="hero-dots"><span class="on"></span><span></span><span></span></div>
</section>

<section class="about">
  <h2 class="section-title">About Us</h2>
  <div class="wrap about-body">
    <div class="about-photo-col">
      <div class="about-photo" role="img" aria-label="Portrait of the doctor and his wife"></div>
      <div class="about-caption">Dr. Daniel Pryor<br>With Wife Helen</div>
    </div>
    <div class="about-info">
      <span class="tag">EDUCATION</span>
      <ul><li>Lone Plains Chiropractic College 1991, Doctor of Chiropractic with honors</li></ul>
      <span class="tag">ADDITIONAL EDUCATION</span>
      <ul>
        <li>Diplomate, Prairie Board of Homeopathic Examiners, 1991</li>
        <li>Diplomate, Meadow Board of Clinical Nutritionists, 1996</li>
        <li>Certified, Clinical Nutritionist, Harrow Academy of Clinical Nutrition, 1996</li>
        <li>Certified, Acupuncture, Lone Plains Chiropractic College, 1999</li>
        <li>Certified, Westfield Academy of Applied Kinesiology, 2004</li>
        <li>Plainsview Board of Chiropractic Internist 180 hours</li>
        <li>Plainsview Board of Chiropractic Neurology 100 hours</li>
        <li>Advanced Kinesiology, Owen Calder DC, 60 hours</li>
        <li>Advanced Kinesiology, Ruth Fenwick DO, 60 hours</li>
      </ul>
      <div class="about-pair">
        <div><span class="tag">LICENSURE</span><ul><li style="margin-bottom:6px">Southplain Board of Chiropractic Examiners</li><li>Mesa Ridge Board of Chiropractic Examiners</li></ul></div>
        <div><span class="tag">MEMBER</span><ul><li>Southplain Chiropractic Association</li></ul></div>
      </div>
    </div>
  </div>
</section>

<section class="testimonials">
  <h2 class="section-title">Testimonial</h2>
  <div class="wrap quote-row">
    <div class="quote">
      <blockquote>I am an M.D. and have advised many of my patients to consult with Dr. Pryor. They see how his advice gets them better quickly. I personally have used his services on many occasions and always found relief for my conditions, and I have seen many patients helped who would otherwise have relied on medications with side effects.</blockquote>
      <cite>RTW, M.D., Mesa Hollow TX</cite>
    </div>
    <div class="quote">
      <blockquote>Prior to seeing Dr. Pryor, I had a headache for 16 straight days as well as lower back and hip pain. The care I received was very professional and I was given a choice of treatment. Now I have no headaches at all, and my back pain is gone. Dr. Pryor and his staff were courteous, kind and caring. The care was simple and very much worth the trip!</blockquote>
      <cite>MA, Mesa Hollow, TX</cite>
    </div>
  </div>
</section>

<section class="faqs" role="region" aria-label="Frequently asked questions, set over a soft photo of a patient receiving care">
  <h2 class="section-title">FAQs</h2>
  <div class="faq-grid">
    <div class="faq"><h3>WHY USE US?</h3><p>Dr. Pryor has over 20 years of experience in chiropractic medicine. He has pursued post graduate work in acupuncture, applied kinesiology, nutrition, herbology and homeopathy. His main goal is to get you well.</p><div class="more-line"><span>+</span></div></div>
    <div class="faq"><h3>DO YOU TAKE INSURANCE?</h3><p>Yes! We take nearly all forms of major medical insurance, medicare and supplements, and auto insurance. Our front desk handles insurance questions and will be happy to help you with any questions you may have.</p><div class="more-line"><span>+</span></div></div>
    <div class="faq"><h3>DO I HAVE TO KEEP COMING BACK ALL THE TIME?</h3><p>No! Dr. Pryor's goal is to see you get well, and get well as fast as possible. He will outline a treatment plan that is reasonable for the complexity and duration of the issue you have been suffering with.</p><div class="more-line"><span>+</span></div></div>
    <div class="faq"><h3>DO YOU TREAT AUTO ACCIDENT INJURIES?</h3><p>Yes! The trauma from an auto accident damages the deeper tissues along the spine, setting up the potential for chronic pain for years to come. It is important to have the tools to work deeper in the system.</p><div class="more-line"><span>+</span></div></div>
    <div class="faq"><h3>DO YOU TREAT SPORTS INJURIES?</h3><p>Yes! The dynamics of a sports injury often need the ability to diagnose the injury on a deeper level. After scans, treatment and time to heal, there is often a residual weakness that persists unexplained.</p><div class="more-line"><span>+</span></div></div>
    <div class="faq"><h3>DO YOU TREAT PREGNANT WOMEN?</h3><p>Yes! Pregnancy places new strain on the spine, hips and deeper tissues, setting up the potential for pain that lingers. Gentle care helps restore balance and comfort for both mother and baby.</p><div class="more-line"><span>+</span></div></div>
  </div>
</section>

<section class="services">
  <h2 class="section-title">Our Services</h2>
  <div class="service-grid">
    <div class="service"><div class="service-photo" role="img" aria-label="Woman holding her head with a headache" style="background:linear-gradient(160deg,#d9c7b8,#8a6e5c)"></div><h3>HEADACHES</h3><p>Chronic headaches and migraines afflict many Americans. The pain affects their families and jobs. Common causes are structural, chemical and allergies.</p></div>
    <div class="service"><div class="service-photo" role="img" aria-label="Woman rubbing a sore shoulder" style="background:linear-gradient(160deg,#e2cbb6,#a27a5e)"></div><h3>SHOULDER PAIN</h3><p>Shoulder and arm pain can be due to overuse, trauma or arthritis, but often it arises from nerve impingement in the neck, where these nerves begin.</p></div>
    <div class="service"><div class="service-photo" role="img" aria-label="Person holding their lower back in pain" style="background:linear-gradient(160deg,#c9b5a2,#5e4638)"></div><h3>LOWER BACK</h3><p>Low back pain is a leading cause of seeking medical care. It may be an acute strain from yard work or a chronic problem you have lived with for years.</p></div>
    <div class="service"><div class="service-photo" role="img" aria-label="Person holding a painful knee" style="background:linear-gradient(160deg,#e6e6e6,#8f9aa3)"></div><h3>KNEE PAIN</h3><p>Knee pain is deeply concerning to athletes and to anyone who wonders how they will get around if a knee gives out. Balance of the joint is key.</p></div>
    <div class="service"><div class="service-photo" role="img" aria-label="Woman with aching neck and shoulders" style="background:linear-gradient(160deg,#3d3a3a,#b59378)"></div><h3>FIBROMYLGIA</h3><p>Fibromyalgia is the diagnosis given to generalized chronic muscle pain. Not long ago many doubted it existed. Now the diagnosis is common.</p></div>
    <div class="service"><div class="service-photo" role="img" aria-label="Woman holding her sore neck" style="background:linear-gradient(160deg,#e8d6c6,#b08a6c)"></div><h3>NECK PAIN</h3><p>Neck pain affects us all at some time. We often reach for pain relievers, yet neck pain can be deeper than brief tension: arthritis or disc wear.</p></div>
  </div>
  <a class="btn-outline" href="#">LEARN MORE</a>
</section>

<section class="other">
  <h2 class="section-title">Other Services</h2>
  <div class="side-arrow left"><svg width="10" height="12" viewBox="0 0 10 12"><polygon points="8,0 0,6 8,12" fill="#fff"/></svg></div>
  <div class="other-grid">
    <div class="other-item"><div class="other-circle" role="img" aria-label="Illustration of a human spine" style="background:radial-gradient(circle,#8fc5ec,#2a4f86)"></div><h3>CHIROPRACTIC</h3><p>As a Chiropractor, Dr. Pryor focuses on disorders of the musculoskeletal system</p><a class="btn-blue" href="#">LEARN MORE</a></div>
    <div class="other-item"><div class="other-circle" role="img" aria-label="Acupuncture needles placed on a patient's back" style="background:radial-gradient(circle,#e4c2a6,#8f6a52)"></div><h3>ACUPUNCTURE</h3><p>The term "acupuncture" describes a family of procedures involving stimulation</p><a class="btn-blue" href="#">LEARN MORE</a></div>
    <div class="other-item"><div class="other-circle" role="img" aria-label="Homeopathic pills beside a green leaf" style="background:radial-gradient(circle,#f1f1ea,#7fa64e)"></div><h3>HOMEOPATHY</h3><p>Homeopathy is a system of medical therapy that uses very small doses of a remedy</p><a class="btn-blue" href="#">LEARN MORE</a></div>
  </div>
  <div class="side-arrow right"><svg width="10" height="12" viewBox="0 0 10 12"><polygon points="2,0 10,6 2,12" fill="#fff"/></svg></div>
</section>

<footer class="site-footer">
  <div class="wrap footer-cols">
    <div><h4>QUICK LINKS</h4><ul class="quick-links"><li>Home</li><li>About Us</li><li>Testimonials</li><li>Faqs</li><li>Resources</li><li>Contact Us</li></ul></div>
    <div class="contact-list"><h4>CONTACT US</h4>
      <p>Daniel Pryor DC PA<br>418 Larkspur Row<br>Mesa Hollow, TX 70001</p>
      <div><i></i>555.014.2290</div><div><i></i>555.014.2291</div><div><i></i>info@birchwellclinic.net</div><div><i></i>www.birchwellclinic.net</div>
    </div>
    <div><h4>MAP</h4><div class="map" role="img" aria-label="Street map showing the clinic location"></div></div>
    <div><h4>FOLLOW US ON</h4>
      <div class="follow-icons"><span></span><span></span><span></span><span></span></div>
      <div class="badge-row"><span></span></div>
      <div class="footer-call">CALL US ON<br>555.014.2290</div>
    </div>
  </div>
</footer>
<div class="footer-bar">© 2016 birchwellclinic.net | Privacy Policy | User Agreement</div>

</body>
</html>
```